Luminously Grounded Vitality

We want to design a business card that is modern and appealing for an innovative psychedelic telemedicine company that provides at-home ketamine-assisted therapy along with wellness, longevity, and anti-aging medicines. We want to use our deep purple and white plus other colors you can find on our website. We don't have any strict brand guidelines yet so feel free to get creative. We want a very professional, but technology first modern design that will instill trust, peace, calm, but also be attractive to investors in the healthcare and SaaS space.

```html
<!DOCTYPE html>
<html lang="en">
<head>
<meta charset="utf-8">
<title>Luminously Grounded Vitality – Business Card</title>
<link rel="stylesheet" href="https://fonts.googleapis.com/css2?family=Montserrat:wght@400;500;600&display=swap">
<style>
  :root {
    --backdrop: #2a2d31;
    --frame-orchid: #b264a8;
    --card-white: #ffffff;
    --brand-violet: #8d6fbd;
    --brand-violet-light: #b49ae0;
    --name-magenta: #a453a0;
    --ink: #3a3a3f;
  }
  * { margin: 0; padding: 0; box-sizing: border-box; }
  html, body { width: 1200px; height: 900px; overflow: hidden; }
  body {
    background: var(--backdrop);
    font-family: "Montserrat", sans-serif;
    display: flex;
    align-items: center;
    justify-content: center;
    gap: 60px;
  }
  .card {
    position: relative;
    width: 460px;
    height: 460px;
  }
  .card-shape { position: absolute; inset: 0; width: 100%; height: 100%; }
  .card-content {
    position: absolute;
    inset: 0;
    display: flex;
    flex-direction: column;
    align-items: center;
    justify-content: flex-start;
    text-align: center;
    padding-top: 108px;
  }
  .brand {
    display: flex;
    align-items: center;
    gap: 7px;
    color: var(--brand-violet);
    font-weight: 500;
    font-size: 16px;
    line-height: 19px;
    margin-bottom: 14px;
  }
  .brand-dot {
    width: 13px; height: 13px;
    border-radius: 50%;
    background: var(--brand-violet);
  }
  .person-name {
    color: var(--name-magenta);
    font-weight: 600;
    font-size: 20px;
    line-height: 24px;
    letter-spacing: 0.5px;
  }
  .person-title {
    color: var(--ink);
    font-size: 13px;
    line-height: 16px;
    margin-top: 4px;
    margin-bottom: 10px;
  }
  .contact-icons { display: flex; gap: 10px; margin-bottom: 8px; }
  .contact-icons svg { width: 22px; height: 22px; }
  .contact-line { color: var(--ink); font-size: 12px; line-height: 18px; }
  .back-content { justify-content: center; padding-top: 0; }
  .back-name {
    color: var(--brand-violet-light);
    font-weight: 500;
    font-size: 30px;
    line-height: 1.25;
    display: flex;
    flex-direction: column;
    align-items: center;
    gap: 14px;
  }
  .back-dot {
    width: 26px; height: 26px;
    border-radius: 50%;
    background: var(--brand-violet-light);
  }
</style>
</head>
<body>
  <svg width="0" height="0" style="position:absolute">
    <defs>
      <g id="cloud-outer">
        <circle cx="140" cy="160" r="125"/>
        <circle cx="320" cy="160" r="125"/>
        <circle cx="230" cy="300" r="125"/>
        <circle cx="230" cy="210" r="110"/>
      </g>
      <g id="cloud-inner">
        <circle cx="140" cy="160" r="110"/>
        <circle cx="320" cy="160" r="110"/>
        <circle cx="230" cy="300" r="110"/>
        <circle cx="230" cy="210" r="100"/>
      </g>
    </defs>
  </svg>

  <section class="card card-back" aria-label="Card back">
    <svg class="card-shape" viewBox="0 0 460 460">
      <use href="#cloud-outer" fill="var(--brand-violet)"/>
    </svg>
    <div class="card-content back-content">
      <p class="back-name"><span class="back-dot"></span>Luminously Grounded<br>Vitality</p>
    </div>
  </section>

  <section class="card card-front" aria-label="Card front">
    <svg class="card-shape" viewBox="0 0 460 460">
      <use href="#cloud-outer" fill="var(--frame-orchid)"/>
      <use href="#cloud-inner" fill="var(--card-white)"/>
    </svg>
    <div class="card-content">
      <p class="brand"><span class="brand-dot"></span>Luminously Grounded Vitality</p>
      <h1 class="person-name">DANIEL OKAFOR</h1>
      <p class="person-title">Development Manager Officer</p>
      <div class="contact-icons">
        <svg viewBox="0 0 24 24" aria-label="Phone"><circle cx="12" cy="12" r="11" fill="none" stroke="var(--name-magenta)" stroke-width="1.6"/><path d="M8.5 7.5c.5-.5 1.2-.4 1.5.1l.9 1.5c.2.4.1.9-.2 1.2l-.6.5c.5 1.2 1.4 2.1 2.6 2.6l.5-.6c.3-.3.8-.4 1.2-.2l1.5.9c.5.3.6 1 .1 1.5l-.6.6c-.6.6-1.6.7-2.4.3-2.200-1.1-3.9-2.8-5-5-.4-.8-.3-1.8.3-2.4z" fill="var(--name-magenta)"/></svg>
        <svg viewBox="0 0 24 24" aria-label="Email"><circle cx="12" cy="12" r="11" fill="var(--name-magenta)"/><rect x="6.5" y="8" width="11" height="8" rx="1" fill="#fff"/><path d="M6.5 8.5l5.5 4 5.5-4" fill="none" stroke="var(--name-magenta)" stroke-width="1.2"/></svg>
        <svg viewBox="0 0 24 24" aria-label="Website"><circle cx="12" cy="12" r="11" fill="none" stroke="var(--name-magenta)" stroke-width="1.6"/><circle cx="12" cy="12" r="6" fill="none" stroke="var(--name-magenta)" stroke-width="1.2"/><path d="M6 12h12M12 6c-2.5 3-2.5 9 0 12M12 6c2.5 3 2.5 9 0 12" fill="none" stroke="var(--name-magenta)" stroke-width="1"/></svg>
      </div>
      <p class="contact-line">555-210-4387</p>
      <p class="contact-line">daniel.okafor@groundedvitality.com</p>
      <p class="contact-line">groundedvitality.com</p>
    </div>
  </section>
</body>
</html>
```